INNOVATIVE DESIGN NEEDED FOR FINANCIAL COMPANY

INTERNATIONAL FIRM IN HONG KONG NEEDS A MODERN BUSINESS CARD DESIGN. ONE SIDE ENGLISH OTHER SIDE IN CHINESE. WE ARE OPEN TO CHANGING FONTS AND COLOR. SHOULD BE A CARD THAT IS PROFESSIONAL DEALING WITH HIGH NET WORTH CLIENTELE. BOTH SIDES OF THE CARD WILL BE THE SAME, HOWEVER, THE WORDING ON ONE SIDE WILL BE ENGLISH AND THE OTHER SIDE IN CHINESE (CAN ASSIST IN THE LETTERING - CAN PROVIDE ONCE CARD DESIGN IS ACCEPTED.

Target Market(s)

Hong Kong/CHINA

Contact Information for Business Card

ATTRACTIVE MODERN

```html
<!DOCTYPE html>
<html lang="en">
<head>
<meta charset="utf-8">
<title>Larch Asset Management – Business Card</title>
<link rel="stylesheet" href="https://fonts.googleapis.com/css2?family=Arimo:wght@400;700&family=Noto+Sans+TC:wght@700&display=swap">
<style>
  :root {
    --bg: #dfe3e3;
    --card: #ffffff;
    --green: #0f8a5f;
    --ink: #2b2b2b;
    --ink-soft: #444444;
    --band-grey: #6f7173;
  }
  * { margin: 0; padding: 0; box-sizing: border-box; }
  html, body {
    width: 1200px; height: 906px; overflow: hidden;
    background: var(--bg);
    font-family: "Arimo", Arial, sans-serif;
  }
  .card {
    position: absolute;
    left: 150px; top: 196px;
    width: 900px; height: 514px;
    background: var(--card);
    box-shadow: 0 6px 20px rgba(0,0,0,0.12);
    overflow: hidden;
  }
  .holder {
    position: absolute; left: 76px; top: 134px;
    width: 280px;
  }
  .holder-name {
    color: var(--green);
    font-weight: 700;
    font-size: 23px;
    letter-spacing: 0.3px;
    line-height: 1;
    white-space: nowrap;
  }
  .holder-title {
    color: var(--ink-soft);
    font-size: 17px;
    margin-top: 3px;
  }
  .brand {
    position: absolute; left: 380px; top: 104px;
    display: flex; align-items: center; gap: 14px;
  }
  .brand-dot {
    width: 72px; height: 72px; border-radius: 50%;
    background: var(--green);
    flex: none;
  }
  .brand-name { color: var(--ink); font-weight: 700; line-height: 1; white-space: nowrap; }
  .brand-name-zh {
    font-family: "Noto Sans TC", "Arimo", sans-serif;
    font-size: 30px; letter-spacing: 1.5px;
  }
  .brand-name-en {
    font-size: 14px; letter-spacing: 2.8px; margin-top: 5px;
  }
  .contacts {
    position: absolute; left: 96px; top: 372px;
    list-style: none;
  }
  .contacts li {
    display: flex; align-items: center; gap: 14px;
    font-size: 17px; color: var(--ink); line-height: 24px;
  }
  .contacts svg { width: 15px; height: 15px; fill: var(--green); flex: none; }
  .address {
    position: absolute; right: 70px; top: 336px;
    text-align: right;
    font-size: 17px; color: var(--ink); line-height: 22px;
  }
  .bottom-bands { position: absolute; left: 0; bottom: 0; width: 900px; height: 60px; }
</style>
</head>
<body>
  <div class="card">
    <div class="holder">
      <div class="holder-name">MORGAN ELLWOOD</div>
      <div class="holder-title">General Manager</div>
    </div>

    <div class="brand">
      <div class="brand-dot"></div>
      <div>
        <div class="brand-name brand-name-zh">樺林資產管理有限公司</div>
        <div class="brand-name brand-name-en">Larch Asset Management Ltd</div>
      </div>
    </div>

    <ul class="contacts">
      <li>
        <svg viewBox="0 0 16 16" aria-hidden="true"><path d="M3.2 1.5l2.4 2.6-1.3 1.8c.9 2 2.6 3.8 4.6 4.7l1.8-1.3 2.6 2.4-1.4 2.4C6.4 13.9 2 9.5 1 3z"/></svg>
        (853) 2900-4417
      </li>
      <li>
        <svg viewBox="0 0 16 16" aria-hidden="true"><path d="M1 3h14v10H1z"/><path d="M2 4l6 5 6-5" stroke="#fff" stroke-width="1.4" fill="none"/></svg>
        hello@larchwealth.com
      </li>
      <li>
        <svg viewBox="0 0 16 16" aria-hidden="true"><circle cx="8" cy="8" r="7"/><path d="M1 8h14M8 1c-3 3.5-3 10.5 0 14M8 1c3 3.5 3 10.5 0 14M2.5 4.5h11M2.5 11.5h11" stroke="#fff" stroke-width="1" fill="none"/></svg>
        www.larchwealth.com
      </li>
    </ul>

    <div class="address">
      Units 5-6 Floor 9 Harbourview Centre<br>
      Block 2 Hoi Wang Rd Yau Ma Tei KLN
    </div>

    <svg class="bottom-bands" viewBox="0 0 900 60" preserveAspectRatio="none" aria-hidden="true">
      <polygon points="0,47 548,47 538,60 0,60" fill="var(--band-grey)"/>
      <polygon points="560,30 900,30 900,60 548,60" fill="var(--green)"/>
    </svg>
  </div>
</body>
</html>
```